Need *Plum Crafted* Events Company Website
Bright Harbor Gatherings Website
Need *Plum Crafted* Events Company Website - Events
Creative Brief
Events
www.brightharborgatherings.example
Bright Harbor Gatherings (BHG) is a multi-dimensional event management firm providing all aspects of support and expertise for any special event. By providing upscale and individualized service, our events are unique and tailored around your personal vision, style and budget.
We provide partial and full-service event coordination services for all types of events; specializing in corporate meetings, conferences, receptions, and everyday social events.
We like unique and captivating web design that illustrates the characteristics of our brand and service offerrings. Our logo speaks to a company that is unique and classy with an edge. DISLIKE: Black or extremely dark backgrounds. Too fancy flash applications, Music or any kind of intro, anything that is too elaborate. LIKE: Easy flow and simplicity. I like the mix of soft neutrals
Feminine
neutral tones
pop of red
complementary tones
right side
www.vowlantern.example
www.quillaffairs.example
Will attached websites that we like later Please use the Fonts from my logo: Will attach files I would like for you to use the accent color on my logo as an special accent only so my logo is not overpowered. I am open to navigation placement but it does not give me that option so I selected what I believe is my personal preference.

```html
<!DOCTYPE html>
<html lang="en">
<head>
<meta charset="utf-8">
<title>Bright Harbor Gatherings</title>
<link href="https://fonts.googleapis.com/css2?family=Great+Vibes&family=Open+Sans:ital,wght@0,400;0,700;1,400;1,700&display=swap" rel="stylesheet">
<style>
:root{
  --cream:#efe8dc;
  --cream-dark:#e4dacb;
  --plum:#7c5257;
  --plum-dark:#5e3b40;
  --plum-line:#9a7479;
  --white:#ffffff;
  --ink:#3a2a2c;
  --accent-red:#b3202a;
  --green:#3fa63a;
  --green-dark:#2b7f28;
  --muted:#7a6a66;
  --contact:#c7adb0;
}
*{margin:0;padding:0;box-sizing:border-box}
html,body{width:1200px;height:799px;overflow:hidden}
body{background:var(--cream);font-family:"Open Sans",Arial,sans-serif;color:var(--ink);position:relative}
.page-texture{position:absolute;inset:0;background:radial-gradient(circle at 70% 40%,var(--cream) 0%,var(--cream-dark) 100%)}
.sidebar{position:absolute;left:101px;top:0;width:266px;height:799px;background:var(--plum);
  border-left:3px solid var(--plum-line);border-right:3px solid var(--plum-line);box-shadow:0 0 14px rgba(0,0,0,.35)}
.logo-art{position:absolute;left:75px;top:18px;width:110px;height:250px;
  background:linear-gradient(180deg,rgba(255,255,255,.85),rgba(230,220,215,.7));border-radius:50% 50% 8px 8px/20% 20% 8px 8px;opacity:.9}
.brand-name{position:absolute;left:10px;top:282px;width:240px;text-align:center;font-family:"Great Vibes",cursive;
  font-size:30px;line-height:32px;color:var(--white)}
.main-nav{position:absolute;left:0;top:392px;width:260px;list-style:none;text-align:center}
.main-nav li{font-family:"Great Vibes",cursive;font-size:28px;line-height:37px;color:var(--white)}
.contact{position:absolute;left:24px;top:710px;width:232px;font-size:10.5px;color:var(--contact);line-height:24px}
.contact div{display:flex;align-items:center;gap:8px;white-space:nowrap}
.connect{position:absolute;left:828px;top:24px;display:flex;align-items:center;gap:9px}
.connect span{font-family:"Great Vibes",cursive;font-size:24px;color:var(--ink);margin-right:14px}
.connect i{display:block;width:28px;height:28px;border-radius:4px;background:var(--plum)}
.stage{position:absolute;left:372px;top:72px;width:727px;height:660px;background:var(--white);padding:10px;box-shadow:0 2px 10px rgba(0,0,0,.25)}
.hero-photo{width:100%;height:100%;background:
  linear-gradient(160deg,#b9a98d 0%,#8c7356 25%,#5e4635 55%,#7b6650 75%,#c9b79e 100%)}
.welcome{position:absolute;left:257px;top:29px;width:456px;height:235px;background:rgba(255,255,255,.55);
  border:1px solid rgba(255,255,255,.8);border-radius:6px;padding:16px 20px;box-shadow:0 0 10px rgba(255,255,255,.5)}
.welcome h1{font-size:19px;font-style:italic;font-weight:700;color:var(--ink);margin-bottom:10px}
.welcome p{font-size:12.2px;font-style:italic;line-height:15px;color:var(--ink);margin-bottom:11px}
.play-btn{position:absolute;right:34px;bottom:10px;width:190px;height:33px;border-radius:17px;
  background:linear-gradient(var(--green),var(--green-dark));color:var(--white);font-size:12px;font-weight:700;
  display:flex;align-items:center;justify-content:center;gap:10px}
.play-btn b{width:16px;height:16px;border-radius:50%;background:var(--white);display:flex;align-items:center;justify-content:center}
.services{position:absolute;top:466px;left:19px;display:flex;gap:34px}
.service-card{width:204px;height:153px;background:var(--white);padding:6px;box-shadow:0 2px 6px rgba(0,0,0,.35)}
.service-card .thumb{height:98px}
.service-card h2{font-family:"Great Vibes",cursive;font-weight:400;font-size:22px;color:var(--accent-red);text-align:center;margin-top:10px;white-space:nowrap}
.thumb-meeting{background:linear-gradient(135deg,#d8d8dc,#5c6070)}
.thumb-seminar{background:linear-gradient(135deg,#d9c7a4,#7d6a52)}
.thumb-wedding{background:linear-gradient(135deg,#dcd4e8,#8a74a8)}
.footer{position:absolute;top:761px;left:396px;width:703px;display:flex;justify-content:space-between;font-size:10.5px;font-style:italic;color:var(--muted)}
</style>
</head>
<body>
<div class="page-texture"></div>

<aside class="sidebar">
  <div class="logo-art" role="img" aria-label="Brand illustration of a statue figure on a pedestal"></div>
  <div class="brand-name">Bright Harbor<br>Gatherings</div>
  <ul class="main-nav">
    <li>Home</li><li>About Us</li><li>Services</li><li>Contact Us</li><li>Events</li><li>Our Blog</li>
  </ul>
  <div class="contact">
    <div><svg width="14" height="12" viewBox="0 0 14 12"><path d="M1 4c0-2 3-3 6-3s6 1 6 3v1H10V3.5H4V5H1z M3 6h8l1 5H2z" fill="#c7adb0"/></svg>(555) 014-2290</div>
    <div><svg width="14" height="10" viewBox="0 0 14 10"><rect x=".5" y=".5" width="13" height="9" fill="none" stroke="#c7adb0"/><path d="M.5.5 7 6l6.5-5.5" fill="none" stroke="#c7adb0"/></svg>info@brightharborgatherings.example</div>
  </div>
</aside>

<div class="connect"><span>Connect with us :</span><i></i><i></i><i></i></div>

<main class="stage">
  <div class="hero-photo" role="img" aria-label="Elegant dining table set with wine glasses, napkins and candles"></div>
  <section class="welcome">
    <h1>Welcome to Bright Harbor Gatherings</h1>
    <p>Bright Harbor Gatherings (BHG) is a multi-dimensional event management firm providing all aspects of support and expertise for any special event. By providing upscale and individualized service, our events are unique and tailored around your personal vision, style and budget.</p>
    <p>We provide partial and full-service event coordination services for all types of events; specializing in corporate meetings, conferences, receptions, and everyday social events.</p>
    <div class="play-btn"><b><svg width="8" height="8" viewBox="0 0 8 8"><path d="M1 0l7 4-7 4z" fill="#2b7f28"/></svg></b>PLAY INTRO</div>
  </section>
  <section class="services">
    <article class="service-card"><div class="thumb thumb-meeting" role="img" aria-label="Business team in a corporate meeting"></div><h2>Corporate Meetings</h2></article>
    <article class="service-card"><div class="thumb thumb-seminar" role="img" aria-label="Conference hall with seated audience"></div><h2>Seminars &amp; Conferences</h2></article>
    <article class="service-card"><div class="thumb thumb-wedding" role="img" aria-label="Decorated wedding reception hall"></div><h2>Weddings &amp; Receptions</h2></article>
  </section>
</main>

<footer class="footer">
  <span>Home | About Us | Services | Contact Us | Events | Our Blog</span>
  <span>Copyright © 2011, Bright Harbor Gatherings. All rights reserved.</span>
</footer>
</body>
</html>
```